Optometrist A5 flyer update 2014

We are an optical / optometrist business needing an existing A5 flyer updated. This flyer has been very successful but needs to be renewed.
We are supplying all the original source files including images.
I have included pdf files with annotations on the alteration we would like made.
We are open to suggestions / alterations to the design of the pamphlet.
We are after a modern design appealing to the various ages of our patient base.

```html
<!DOCTYPE html>
<html lang="en">
<head>
<meta charset="utf-8">
<title>Frequently Asked Questions – Optometrist Flyer</title>
<link rel="stylesheet" href="https://fonts.googleapis.com/css2?family=Source+Sans+3:wght@400;600;700&display=swap">
<style>
  :root {
    --paper: #ffffff;
    --panel-top: #4fa3dd;
    --panel-bottom: #1570c0;
    --ink-light: #ffffff;
    --ink-soft: #eef5fc;
    --rule: rgba(255, 255, 255, 0.75);
    --note-red: #e0233a;
    --frame-dark: #2a2a2e;
    --frame-wine: #6b1f22;
    --chart-ink: #c9d6e6;
    --icon-fill: #1b6fc0;
  }
  * { box-sizing: border-box; margin: 0; padding: 0; }
  html, body { width: 866px; height: 1200px; overflow: hidden; background: var(--paper); }
  body { font-family: "Source Sans 3", sans-serif; }

  .flyer { position: relative; width: 866px; height: 1200px; background: var(--paper); overflow: hidden; }

  /* Left photo column */
  .photo { position: absolute; left: 0; width: 420px; }
  .photo--frames-rimless { top: 0; height: 182px; background: linear-gradient(180deg, #f4f4f5 0%, #dcdde0 55%, #f6f6f7 100%); }
  .photo--frames-wine { top: 191px; height: 224px; background: linear-gradient(160deg, #f5f2f2 0%, #c9a3a4 45%, #8a3b3e 60%, #f3eeee 100%); }
  .photo--frames-halfrim { top: 647px; height: 242px; left: 22px; width: 398px; background: linear-gradient(170deg, #f4f4f6 0%, #c7c5cc 45%, #4a4550 58%, #f2f1f4 100%); }
  .photo--eye-chart { top: 889px; height: 311px; background: linear-gradient(170deg, #ffffff 0%, #eef2f7 40%, #d6dfeb 70%, #f7f9fb 100%); }

  .placeholder-note {
    position: absolute; left: 88px; top: 516px;
    font-size: 21px; font-weight: 400; color: var(--note-red);
  }

  /* Right FAQ panel */
  .faq-panel {
    position: absolute; left: 420px; top: 0; width: 446px; height: 1200px;
    background: linear-gradient(180deg, var(--panel-top) 0%, #3389d0 45%, var(--panel-bottom) 100%);
    color: var(--ink-light);
  }
  .faq-title {
    position: absolute; left: 22px; top: 76px;
    font-size: 29px; font-weight: 600; letter-spacing: 0.1px;
  }
  .faq-item { position: absolute; left: 22px; width: 410px; }
  .faq-question {
    display: flex; align-items: flex-start; gap: 10px;
    font-size: 21px; font-weight: 700; line-height: 25px;
  }
  .faq-question svg { flex: 0 0 30px; margin-top: -2px; }
  .faq-answer {
    margin: 18px 0 0 42px; width: 318px;
    font-size: 16.5px; line-height: 26.5px; color: var(--ink-soft);
  }
  .faq-answer--justified { text-align: justify; }

  .faq-item--sunglasses { top: 155px; }
  .faq-item--refit { top: 390px; }
  .faq-item--health-fund { top: 642px; }

  .divider { position: absolute; left: 29px; top: 891px; width: 354px; height: 1px; background: var(--rule); }

  .hours { position: absolute; left: 62px; top: 918px; }
  .hours-title { font-size: 21px; font-weight: 700; margin-bottom: 18px; }
  .hours-table { border-collapse: collapse; font-size: 17px; color: var(--ink-soft); }
  .hours-table td { padding: 0; height: 26.6px; }
  .hours-table td.day { width: 106px; }
</style>
</head>
<body>
<div class="flyer">

  <div class="photo photo--frames-rimless" role="img" aria-label="Photo of slim black metal semi-rimless spectacle frames"></div>
  <div class="photo photo--frames-wine" role="img" aria-label="Photo of wine-red metal spectacle frames with black temples"></div>
  <p class="placeholder-note">Sunglass image required here</p>
  <div class="photo photo--frames-halfrim" role="img" aria-label="Photo of black half-rim spectacle frames"></div>
  <div class="photo photo--eye-chart" role="img" aria-label="Photo of an eye test chart with letters in perspective"></div>

  <section class="faq-panel">
    <h1 class="faq-title">Frequently Asked Questions?</h1>

    <article class="faq-item faq-item--sunglasses">
      <h2 class="faq-question">
        <svg width="30" height="30" viewBox="0 0 30 30" aria-hidden="true"><circle cx="15" cy="15" r="15" fill="var(--icon-fill)"/><path d="M10 8 L21 15 L10 22" fill="none" stroke="#fff" stroke-width="3"/></svg>
        <span>Can I have fashion sunglasses made to my prescription?</span>
      </h2>
      <p class="faq-answer">Yes. It does depend on the sunglasses and your prescription. We offer a range of sunglasses that can be fitted with prescription lenses.</p>
    </article>

    <article class="faq-item faq-item--refit">
      <h2 class="faq-question">
        <svg width="30" height="30" viewBox="0 0 30 30" aria-hidden="true"><circle cx="15" cy="15" r="15" fill="var(--icon-fill)"/><path d="M10 8 L21 15 L10 22" fill="none" stroke="#fff" stroke-width="3"/></svg>
        <span>If I want new prescription lenses fitted to my existing pair of glasses, do I have to go without them for a week?</span>
      </h2>
      <p class="faq-answer">No. We can usually fit new lenses to your own frame onsite. You only need to be without your glasses for a few hours.</p>
    </article>

    <article class="faq-item faq-item--health-fund">
      <h2 class="faq-question">
        <svg width="30" height="30" viewBox="0 0 30 30" aria-hidden="true"><circle cx="15" cy="15" r="15" fill="var(--icon-fill)"/><path d="M10 8 L21 15 L10 22" fill="none" stroke="#fff" stroke-width="3"/></svg>
        <span>Do I have to purchase my spectacles where my private health fund directs ?</span>
      </h2>
      <p class="faq-answer faq-answer--justified">No. It is your decision where to have your eyes tested and where to purchase your spectacles or contact lenses. We can direct bill your private health fund with the ClaimLink system.</p>
    </article>

    <div class="divider"></div>

    <div class="hours">
      <h2 class="hours-title">Opening Hours:</h2>
      <table class="hours-table">
        <tr><td class="day">Monday</td><td>9.00am - 5.30pm</td></tr>
        <tr><td class="day">Tuesday</td><td>9.00am - 6.30pm</td></tr>
        <tr><td class="day">Wednesday</td><td>9.00am - 5.30pm</td></tr>
        <tr><td class="day">Thursday</td><td>9.00am - 6.30pm</td></tr>
        <tr><td class="day">Friday</td><td>9.00am - 5.30pm</td></tr>
        <tr><td class="day">Saturday</td><td>9.00am - 1.00pm</td></tr>
      </table>
    </div>
  </section>

</div>
</body>
</html>
```